MUSIC FESTIVAL 2023

On the occasion of the 2023 music festival, the 24th, brings the BRUMEVENT group to its terrace.
We are organizing a giant barbecue on this occasion.
This event is organized in collaboration with LE MORVAN.
Possibility of take-out!
Address of the event: 11-15 Place Gustave Morlet in CAMBRAI.4
From 19h.
03 41 56 92 17 - kevin@orchidee-logis.example
Please write in French.
To use the logos of the two establishments.

```html
<!DOCTYPE html>
<html lang="fr">
<head>
<meta charset="utf-8">
<title>Brumevent – Fête de la Musique 2023</title>
<link rel="stylesheet" href="https://fonts.googleapis.com/css2?family=Staatliches&family=Bebas+Neue&family=Poppins:wght@200;300;400;500;600;700&display=swap">
<style>
  :root {
    --ink: #161616;
    --ink-soft: #222222;
    --panel: #3a3a3a;
    --orange: #e2502c;
    --white: #ffffff;
    --silver-light: #f2f2f2;
    --silver-mid: #b9b9b9;
    --silver-dark: #8a8a8a;
    --meat-dark: #3b2118;
    --meat-light: #8a4a32;
  }
  * { margin: 0; padding: 0; box-sizing: border-box; }
  html, body {
    width: 865px; height: 1200px; overflow: hidden;
    background: var(--ink);
  }
  .flyer {
    position: relative;
    width: 865px; height: 1200px; overflow: hidden;
    background:
      radial-gradient(ellipse 320px 520px at 180px 520px, rgba(120,120,120,0.18), transparent 70%),
      radial-gradient(ellipse 300px 260px at 720px 60px, rgba(90,90,90,0.2), transparent 70%),
      var(--ink);
    font-family: "Poppins", sans-serif;
    color: var(--white);
  }
  .band-name {
    position: absolute; left: 60px; top: 60px;
    width: 210px; height: 990px;
  }
  .band-name text {
    font-family: "Staatliches", sans-serif;
    font-size: 262px;
  }
  .occasion {
    position: absolute; left: 334px; top: 70px;
    font-size: 19px; font-weight: 400; letter-spacing: 6px;
  }
  .year-big {
    position: absolute; left: 328px; top: 92px;
    font-size: 136px; font-weight: 200; letter-spacing: 8px;
    line-height: 1; color: var(--orange);
  }
  .festival {
    position: absolute; left: 334px; top: 222px;
    font-family: "Bebas Neue", sans-serif;
    font-size: 42px; letter-spacing: 0.5px; line-height: 1;
  }
  .collab-label {
    position: absolute; left: 334px; top: 322px;
    font-size: 14px; font-weight: 500; letter-spacing: 3.4px;
    color: var(--orange);
  }
  .partner-name {
    position: absolute; left: 334px; top: 356px;
    font-size: 40px; font-weight: 600; letter-spacing: 1px; line-height: 1;
  }
  .month {
    position: absolute; left: 334px; top: 494px;
    font-family: "Bebas Neue", sans-serif;
    font-size: 56px; line-height: 1; color: var(--orange);
  }
  .day-box {
    position: absolute; left: 332px; top: 548px;
    width: 198px; height: 202px;
    background: var(--panel);
    display: flex; align-items: center; justify-content: center;
    font-family: "Bebas Neue", sans-serif;
    font-size: 210px; line-height: 1; padding-top: 18px;
  }
  .date-foot {
    position: absolute; left: 334px; top: 760px;
    display: flex; align-items: center; gap: 12px;
  }
  .date-year {
    font-size: 36px; font-weight: 200; letter-spacing: 5px; line-height: 1;
  }
  .time-tag {
    background: var(--orange);
    padding: 3px 8px 1px;
    font-size: 18px; font-weight: 400; line-height: 1.2;
  }
  .time-tag b { font-family: "Bebas Neue", sans-serif; font-weight: 400; font-size: 21px; }
  .bbq { position: absolute; left: 336px; top: 848px; }
  .bbq-lead { font-size: 18px; font-weight: 400; letter-spacing: 1.4px; }
  .bbq-title {
    font-size: 30px; font-weight: 700; line-height: 1.08; letter-spacing: 0.5px;
  }
  .bbq-tail {
    font-size: 15px; letter-spacing: 5px; color: var(--orange); margin-top: 2px;
  }
  .address {
    position: absolute; left: 336px; top: 1004px;
    display: flex; align-items: center; gap: 10px;
    font-size: 18px; font-weight: 500; line-height: 1.22;
  }
  .address svg { width: 28px; height: 40px; flex: none; }
  .footer {
    position: absolute; left: 68px; top: 1080px;
    display: flex; align-items: center; height: 74px;
  }
  .host {
    display: flex; align-items: center; gap: 8px;
    font-size: 13px; font-weight: 600; width: 102px; line-height: 1.15;
  }
  .host-dot { width: 12px; height: 12px; border-radius: 50%; background: var(--white); flex: none; }
  .footer-rule { width: 1px; height: 74px; background: var(--orange); margin: 0 18px 0 8px; }
  .contact-label { font-size: 12.5px; font-weight: 500; letter-spacing: 1px; }
  .contact-line { display: flex; gap: 24px; font-size: 14px; font-weight: 300; margin-top: 3px; }
  .contact-line span { display: flex; align-items: center; gap: 4px; }
  .contact-line svg { width: 11px; height: 11px; fill: var(--orange); }
  .photo-meat {
    position: absolute; left: 665px; top: 148px;
    width: 200px; height: 400px;
    border-radius: 80px 0 0 90px;
    background: radial-gradient(ellipse at 45% 45%, var(--meat-light), var(--meat-dark) 60%, transparent 78%);
  }
  .illustration-guitar {
    position: absolute; left: 620px; top: 0;
    width: 245px; height: 1200px;
    background:
      linear-gradient(to bottom, transparent 0, transparent 570px, var(--orange) 600px, var(--orange) 100%);
    border-radius: 0;
    clip-path: polygon(100% 0, 85% 0, 85% 600px, 30% 620px, 8% 800px, 2% 1000px, 20% 1200px, 100% 1200px);
  }
</style>
</head>
<body>
<main class="flyer">
  <svg class="band-name" viewBox="0 0 210 990" aria-label="BRUMEVENT">
    <defs>
      <linearGradient id="silver" x1="0" y1="0" x2="1" y2="0.3">
        <stop offset="0" stop-color="var(--silver-light)"/>
        <stop offset="0.35" stop-color="var(--silver-mid)"/>
        <stop offset="0.6" stop-color="var(--silver-light)"/>
        <stop offset="1" stop-color="var(--silver-dark)"/>
      </linearGradient>
    </defs>
    <text transform="translate(200 985) rotate(-90)" textLength="980" lengthAdjust="spacingAndGlyphs" fill="url(#silver)">BRUMEVENT</text>
  </svg>

  <div class="photo-meat" role="img" aria-label="Photo de viandes grillées au barbecue"></div>
  <div class="illustration-guitar" role="img" aria-label="Guitare électrique orange demi-caisse"></div>

  <p class="occasion">À L'OCCASION DE</p>
  <p class="year-big">2023</p>
  <h1 class="festival">FÊTE DE LA MUSIQUE</h1>

  <p class="collab-label">EN COLLABORATION AVEC</p>
  <p class="partner-name">Le Morvan</p>

  <p class="month">DECEMBER</p>
  <div class="day-box">11</div>
  <div class="date-foot">
    <span class="date-year">2023</span>
    <span class="time-tag">From <b>19H</b></span>
  </div>

  <div class="bbq">
    <p class="bbq-lead">NOUS ORGANISONS UN</p>
    <p class="bbq-title">BARBECUE<br>GÉANT À</p>
    <p class="bbq-tail">CETTE OCCASION</p>
  </div>

  <div class="address">
    <svg viewBox="0 0 24 34" aria-hidden="true">
      <path d="M12 0C5.4 0 0 5.2 0 11.8 0 20 12 34 12 34s12-14 12-22.2C24 5.2 18.6 0 12 0zm0 17a5.2 5.2 0 1 1 0-10.4A5.2 5.2 0 0 1 12 17z" fill="var(--orange)"/>
    </svg>
    <p>11-15 Place Gustave<br>Morlet in CAMBRAI.4</p>
  </div>

  <footer class="footer">
    <div class="host"><span class="host-dot"></span>Le Trente-et-Un</div>
    <div class="footer-rule"></div>
    <div class="contact">
      <p class="contact-label">POUR PLUS D'INFORMATIONS CONTACTEZ</p>
      <p class="contact-line">
        <span><svg viewBox="0 0 24 24" aria-hidden="true"><path d="M6.6 10.8a15.1 15.1 0 0 0 6.6 6.6l2.2-2.2a1 1 0 0 1 1-.25 11.4 11.4 0 0 0 3.6.6 1 1 0 0 1 1 1V20a1 1 0 0 1-1 1A17 17 0 0 1 3 4a1 1 0 0 1 1-1h3.5a1 1 0 0 1 1 1 11.4 11.4 0 0 0 .6 3.6 1 1 0 0 1-.25 1z"/></svg>03 41 56 92 17</span>
        <span><svg viewBox="0 0 24 24" aria-hidden="true"><path d="M2 5h20v14H2zm2 2v.5l8 5 8-5V7z"/></svg>kevin@orchidee-logis.example</span>
      </p>
    </div>
  </footer>
</main>
</body>
</html>
```